Simple elegant business card

General card for a fin and television director.
Just want name, email, phone and address.

Target Market(s)

Prospective employers

Industry/Entity Type

Business

Requirements
Must have
• As above
Nice to have
• Logo but not necessary.
Should not have
• Not too colourful or funky.
• Simplicity and elegance the way to go.

```html
<!DOCTYPE html>
<html lang="en">
<head>
<meta charset="utf-8">
<title>Nora Hale – Film Director</title>
<link rel="stylesheet" href="https://fonts.googleapis.com/css2?family=Yanone+Kaffeesatz:wght@400;600;700&display=swap">
<style>
  :root {
    --card-black: #000000;
    --accent-red: #ff0000;
    --text-white: #ffffff;
    --edge-grey: #2a2a2a;
  }
  html, body {
    margin: 0;
    padding: 0;
    width: 1200px;
    height: 667px;
    overflow: hidden;
    background: var(--card-black);
  }
  .card {
    position: relative;
    width: 1200px;
    height: 667px;
    background: var(--card-black);
    box-sizing: border-box;
    border: 1px solid var(--edge-grey);
    font-family: "Yanone Kaffeesatz", "Arial Narrow", sans-serif;
    color: var(--text-white);
  }
  .identity,
  .contact {
    position: absolute;
    right: 38px;
    text-align: right;
  }
  .identity { top: 272px; }
  .identity__name {
    margin: 0;
    font-size: 104px;
    font-weight: 600;
    line-height: 1;
    letter-spacing: 0.5px;
  }
  .identity__role {
    margin: 2px 0 0;
    font-size: 24px;
    font-weight: 600;
    line-height: 1;
  }
  .accent-band {
    position: absolute;
    left: 0;
    top: 465px;
    width: 100%;
    height: 40px;
    background: var(--accent-red);
  }
  .contact {
    top: 536px;
    margin: 0;
    font-style: normal;
    font-size: 40px;
    font-weight: 600;
    line-height: 46px;
  }
  .contact__line { display: block; }
  .contact__label { margin-right: 10px; }
</style>
</head>
<body>
  <main class="card">
    <header class="identity">
      <h1 class="identity__name">Nora Hale</h1>
      <p class="identity__role">Film Director</p>
    </header>
    <div class="accent-band"></div>
    <address class="contact">
      <span class="contact__line"><span class="contact__label">Mobile:</span>+(1) 310 555 0142</span>
      <span class="contact__line"><span class="contact__label">e-mail:</span>norahale@mail.com</span>
    </address>
  </main>
</body>
</html>
```